Design a visually appealing layout for our company mission and values. I want to create a visually appealing 1 page flyer that presents our company mission and values to clients as well as to our internal team/staff. We will utilize the 1 page flyer in internal and external presentations about our company. We will also use the flyer in sales proposals/marketing packages.

Target Market(s)

Internal team members as well as external prospective clients, existing clients & referral partners

Industry/Entity Type

Financial Service

Colors

Designer to choose colors to be used in the design.

Requirements
Must have
• Should reflect our company brand so I have included our Pantone panel, fonts etc. I have provided our company logo as well which should be part of the branded document
Nice to have
• I would like the presentation to be useable in different formats and to different audiences so something that is more graphic/visual heavy - otherwise it's a lot of words that people don't read.
• Would like to be able to easily include in our corporate template powerpoint presentation.

```html
<!DOCTYPE html>
<html lang="en">
<head>
<meta charset="utf-8">
<title>Northbridge Retirement Group – Mission &amp; Value</title>
<link rel="stylesheet" href="https://fonts.googleapis.com/css2?family=Barlow+Condensed:wght@300;400;500;600;700&family=Montserrat:wght@500&display=swap">
<style>
  :root{
    --page:#bcc6cc;
    --navy:#1d3a66;
    --navy-deep:#17305a;
    --band:#3f78b6;
    --band-dark:#2d5f9c;
    --ring:#d3d6d9;
    --link:#3a72b8;
    --text:#1b1b1b;
    --num:#c3c8cf;
    --row:#eeeff1;
    --bar-light:#4d86c4;
    --bar-dark:#2d5a93;
  }
  *{box-sizing:border-box;margin:0;padding:0}
  html,body{width:1200px;height:827px;overflow:hidden;background:var(--page)}
  body{position:relative;font-family:"Barlow Condensed",sans-serif;color:var(--text)}

  .flyer{
    position:absolute;top:53px;width:510px;height:720px;background:#fff;overflow:hidden;
    --c1:#3f7cc4;--c2:#3f7cc4;--c3:#3f7cc4;--c4:#3f7cc4;--c5:#3f7cc4;--c6:#3f7cc4;--c7:#3f7cc4;
    --n1:var(--num);--n2:var(--num);--n3:var(--num);--n4:var(--num);--n5:var(--num);--n6:var(--num);
    --t1:var(--link);--t2:var(--link);--t3:var(--link);--t4:var(--link);--t5:var(--link);--t6:var(--link);--t7:var(--link);
    --headline:var(--navy);
  }
  .flyer--blue{left:64px}
  .flyer--color{
    left:627px;
    --c1:#8dc63f;--c2:#a44a1c;--c3:#3b6a2b;--c4:#e2a330;--c5:#9a8b74;--c6:#3f7cc4;--c7:#5b2446;
    --n1:#8dc63f;--n2:#a44a1c;--n3:#3b6a2b;--n4:#e2a330;--n5:#8f8069;--n6:#3f7cc4;
    --t1:#8dc63f;--t2:#a44a1c;--t3:#3b6a2b;--t4:#d9982a;--t5:#8f8069;--t6:#3f7cc4;--t7:#5b2446;
  }

  .backdrop{position:absolute;left:30px;top:0;width:450px;height:290px;
    background:radial-gradient(ellipse at 50% 45%,#e6f0f8 0%,rgba(230,240,248,.5) 45%,rgba(255,255,255,0) 72%)}

  .brand{position:absolute;top:30px;left:0;width:100%;text-align:center}
  .brand__name{display:inline-flex;align-items:center;gap:6px;font-weight:600;font-size:21px;color:var(--navy);letter-spacing:.3px}
  .brand__dot{width:11px;height:11px;border-radius:50%;background:#6aa84f}
  .brand__tag{font-family:"Montserrat",sans-serif;font-weight:500;font-size:5.4px;letter-spacing:1.2px;color:#5a6470;margin-top:4px}

  .headline{position:absolute;left:0;width:100%;text-align:center;color:var(--navy);line-height:1}
  .headline--small{top:90px;font-size:40px;font-weight:500;letter-spacing:.5px}
  .headline--big{top:125px;font-size:83px;font-weight:700;letter-spacing:-.5px;color:var(--headline)}
  .flyer--color .headline--big{background:linear-gradient(180deg,#3f6b4c 0%,#24425f 60%,var(--navy-deep) 100%);-webkit-background-clip:text;background-clip:text;color:transparent}

  .mission{position:absolute;top:206px;left:0;width:100%;height:102px;text-align:center;color:#fff;
    background:linear-gradient(180deg,var(--band) 0%,#3b72b0 100%)}
  .mission__title{font-size:38px;font-weight:500;margin-top:10px;line-height:1}
  .mission__rule{width:33px;height:2px;background:#fff;margin:10px auto 0}
  .mission__text{font-size:15px;font-weight:500;margin-top:13px;letter-spacing:.2px}

  .wheel{position:absolute;left:0;top:300px;width:510px;height:210px}
  .wheel__label{position:absolute;top:308px;left:0;width:100%;text-align:center;color:#fff;line-height:1}
  .wheel__we{font-size:35px;font-weight:400;margin-top:13px}
  .wheel__value{font-size:43px;font-weight:500;margin-top:1px}

  .values{position:absolute;top:510px;left:0;width:100%}
  .values__row{position:relative;height:54px}
  .values__row--shaded{height:105px;background:var(--row);padding-top:2px}
  .value{position:absolute;width:230px}
  .value--left{left:27px}
  .value--right{left:278px}
  .value__num{position:absolute;left:0;top:3px;font-size:40px;font-weight:300;line-height:1}
  .value__body{margin-left:23px}
  .value__title{font-size:11px;font-weight:600;text-decoration:underline;line-height:1.2}
  .value__text{font-size:8.6px;font-weight:500;line-height:1.32;margin-top:1px}
  .flyer--color .value__num{font-weight:600}

  .closing{position:absolute;top:682px;left:0;width:100%;text-align:center}
  .closing__title{font-size:11px;font-weight:600;text-decoration:underline;color:var(--t7)}
  .closing__text{font-size:8.6px;font-weight:500;margin-top:3px}

  .footer-bar{position:absolute;bottom:0;left:0;width:100%;height:6px;
    background:linear-gradient(90deg,var(--bar-light) 0 29%,var(--bar-dark) 29% 70%,var(--bar-light) 70% 100%)}
  .icon-set{position:absolute;width:0;height:0}
</style>
</head>
<body>

<svg class="icon-set" aria-hidden="true">
  <defs>
    <symbol id="i-team" viewBox="-16 -16 32 32">
      <g fill="#fff"><circle cx="-8" cy="-5" r="4"/><circle cx="8" cy="-5" r="4"/><path d="M-16 9c0-6 3-8 8-8s8 2 8 8z"/><path d="M0 9c0-6 3-8 8-8s8 2 8 8z"/><circle cx="0" cy="-2" r="5" stroke="currentColor" stroke-width="1.5"/><path d="M-9 14c0-8 4-10 9-10s9 2 9 10z" stroke="currentColor" stroke-width="1.5"/></g>
    </symbol>
    <symbol id="i-money" viewBox="-16 -16 32 32">
      <text x="0" y="2" text-anchor="middle" font-family="Barlow Condensed,sans-serif" font-weight="700" font-size="22" fill="#fff">$</text>
      <path d="M-15 8c4-2 7-2 10 0h8c2 0 2 3 0 3h-6M-15 14c6-2 12 1 18 0l10-7c2-1 3 1 2 2l-10 8c-6 3-13 1-20 1" fill="none" stroke="#fff" stroke-width="2" stroke-linecap="round"/>
    </symbol>
    <symbol id="i-idea" viewBox="-16 -16 32 32">
      <g fill="#fff"><circle cx="0" cy="-1" r="7"/><rect x="-4" y="5" width="8" height="3"/><rect x="-3" y="9" width="6" height="2" rx="1"/></g>
      <g stroke="#fff" stroke-width="2" stroke-linecap="round"><path d="M0-15v3M-11-1h-3M14-1h-3M-8-10l2 2M8-10l-2 2"/></g>
    </symbol>
    <symbol id="i-gear" viewBox="-16 -16 32 32">
      <circle r="11" fill="none" stroke="#fff" stroke-width="4" stroke-dasharray="4 4.6"/>
      <circle r="8.5" fill="none" stroke="#fff" stroke-width="1.6"/>
      <circle r="4" fill="none" stroke="#fff" stroke-width="1.6"/>
    </symbol>
    <symbol id="i-hands" viewBox="-16 -16 32 32">
      <g fill="#fff"><path d="M-16-6l6-4 9 6-4 4z"/><path d="M16-6l-6-4-11 5 3 3 5-2z"/><path d="M-10 0l6 7c1 1 3 1 4 0l8-6-3-3-6 4-5-5z"/><circle cx="-5" cy="9" r="1.8"/><circle cx="-1" cy="11" r="1.8"/></g>
    </symbol>
    <symbol id="i-shield" viewBox="-16 -16 32 32">
      <path d="M0-15l12 4c0 14-5 22-12 26-7-4-12-12-12-26z" fill="none" stroke="#fff" stroke-width="2.2"/>
      <rect x="-4" y="-1" width="8" height="7" rx="1" fill="#fff"/>
      <path d="M-2.5-1v-3a2.5 2.5 0 0 1 5 0v3" fill="none" stroke="#fff" stroke-width="1.6"/>
    </symbol>
    <symbol id="i-search" viewBox="-16 -16 32 32">
      <circle cx="-4" cy="-4" r="9" fill="none" stroke="#fff" stroke-width="2.4"/>
      <path d="M-9-5a5 5 0 0 1 4-4" fill="none" stroke="#fff" stroke-width="1.4"/>
      <path d="M3 3l10 11" stroke="#fff" stroke-width="4" stroke-linecap="round"/>
    </symbol>
    <radialGradient id="shine" cx="35%" cy="30%" r="75%">
      <stop offset="0" stop-color="#fff" stop-opacity=".28"/>
      <stop offset="1" stop-color="#000" stop-opacity=".12"/>
    </radialGradient>
    <radialGradient id="disc" cx="50%" cy="10%" r="95%">
      <stop offset="0" stop-color="#2c5c98"/>
      <stop offset="1" stop-color="#172f5a"/>
    </radialGradient>
  </defs>
</svg>

<!-- Two colourways of the flyer -->
<section class="flyer flyer--blue" aria-label="Mission and values flyer, blue version">
  <div class="backdrop" role="img" aria-label="Faint world map backdrop"></div>
  <div class="brand">
    <div class="brand__name"><span class="brand__dot"></span>Northbridge Retirement Group</div>
    <div class="brand__tag">PLAN TODAY. SECURE TOMORROW.</div>
  </div>
  <h2 class="headline headline--small">OUR COMPANY</h2>
  <h1 class="headline headline--big">MISSION &amp; VALUE</h1>

  <div class="mission">
    <div class="mission__title">Our Mission</div>
    <div class="mission__rule"></div>
    <p class="mission__text">to proactively support organizations and lead them toward a secure future</p>
  </div>

  <svg class="wheel" viewBox="0 0 510 210">
    <circle cx="255" cy="3" r="166" fill="none" stroke="#c7cdd3" stroke-width="3"/>
    <path d="M135 8A120 120 0 0 0 375 8" fill="none" stroke="var(--ring)" stroke-width="9"/>
    <path d="M144 8A111 111 0 0 0 366 8Z" fill="url(#disc)"/>
    <g>
      <g transform="translate(94 44)"><circle r="31" fill="var(--c1)"/><circle r="27" fill="url(#shine)" stroke="#fff" stroke-width="2.4"/><use href="#i-team" x="-16" y="-16" width="32" height="32" color="var(--c1)"/></g>
      <g transform="translate(127 105)"><circle r="31" fill="var(--c2)"/><circle r="27" fill="url(#shine)" stroke="#fff" stroke-width="2.4"/><use href="#i-money" x="-16" y="-16" width="32" height="32"/></g>
      <g transform="translate(185 152)"><circle r="31" fill="var(--c3)"/><circle r="27" fill="url(#shine)" stroke="#fff" stroke-width="2.4"/><use href="#i-idea" x="-16" y="-16" width="32" height="32"/></g>
      <g transform="translate(255 169)"><circle r="31" fill="var(--c4)"/><circle r="27" fill="url(#shine)" stroke="#fff" stroke-width="2.4"/><use href="#i-gear" x="-16" y="-16" width="32" height="32"/></g>
      <g transform="translate(326 152)"><circle r="31" fill="var(--c5)"/><circle r="27" fill="url(#shine)" stroke="#fff" stroke-width="2.4"/><use href="#i-hands" x="-16" y="-16" width="32" height="32"/></g>
      <g transform="translate(383 105)"><circle r="31" fill="var(--c6)"/><circle r="27" fill="url(#shine)" stroke="#fff" stroke-width="2.4"/><use href="#i-shield" x="-16" y="-16" width="32" height="32"/></g>
      <g transform="translate(415 44)"><circle r="31" fill="var(--c7)"/><circle r="27" fill="url(#shine)" stroke="#fff" stroke-width="2.4"/><use href="#i-search" x="-16" y="-16" width="32" height="32"/></g>
    </g>
  </svg>
  <div class="wheel__label"><div class="wheel__we">WE</div><div class="wheel__value">VALUE</div></div>

  <div class="values">
    <div class="values__row">
      <div class="value value--left"><span class="value__num" style="color:var(--n1)">1</span><div class="value__body"><h3 class="value__title" style="color:var(--t1)">Teamwork</h3><p class="value__text">Collaborating with team members, clients and partners to<br>maintain a high level of communication, accountability and<br>engagement to achieve our common goals.</p></div></div>
      <div class="value value--right"><span class="value__num" style="color:var(--n4)">4</span><div class="value__body"><h3 class="value__title" style="color:var(--t4)">Proactivity</h3><p class="value__text">We hold ourselves accountable in anticipating<br>regulatory changes and keeping you and your<br>plan in compliance.</p></div></div>
    </div>
    <div class="values__row values__row--shaded">
      <div class="value value--left" style="top:2px"><span class="value__num" style="color:var(--n2)">2</span><div class="value__body"><h3 class="value__title" style="color:var(--t2)">Financial Empowerment</h3><p class="value__text">We commit ourselves to providing the best retirement<br>solutions to guide our clients toward financial freedom.</p></div></div>
      <div class="value value--right" style="top:2px"><span class="value__num" style="color:var(--n5)">5</span><div class="value__body"><h3 class="value__title" style="color:var(--t5)">Dedication</h3><p class="value__text">We provide exceptional customer service and ensure<br>that we are friendly, timely and responsive whenever<br>corresponding with our clients.</p></div></div>
      <div class="value value--left" style="top:54px"><span class="value__num" style="color:var(--n3)">3</span><div class="value__body"><h3 class="value__title" style="color:var(--t3)">Knowledge</h3><p class="value__text">Our team of highly trained and credentialed experts work<br>to educate and lead our clients toward success.</p></div></div>
      <div class="value value--right" style="top:54px"><span class="value__num" style="color:var(--n6)">6</span><div class="value__body"><h3 class="value__title" style="color:var(--t6)">Security</h3><p class="value__text">With an emphasis on high technological standards, we<br>lead you toward peace of mind that your savings and<br>investments are protected.</p></div></div>
    </div>
  </div>

  <div class="closing">
    <h3 class="closing__title">Transparency</h3>
    <p class="closing__text">We take pride in representing the retirement plan industry as an open, honest, and socially responsible firm with our clients.</p>
  </div>
  <div class="footer-bar"></div>
</section>

<section class="flyer flyer--color" aria-label="Mission and values flyer, multicolour version">
  <div class="backdrop" role="img" aria-label="Faint world map backdrop"></div>
  <div class="brand">
    <div class="brand__name"><span class="brand__dot"></span>Northbridge Retirement Group</div>
    <div class="brand__tag">PLAN TODAY. SECURE TOMORROW.</div>
  </div>
  <h2 class="headline headline--small">OUR COMPANY</h2>
  <h1 class="headline headline--big">MISSION &amp; VALUE</h1>

  <div class="mission">
    <div class="mission__title">Our Mission</div>
    <div class="mission__rule"></div>
    <p class="mission__text">to proactively support organizations and lead them toward a secure future</p>
  </div>

  <svg class="wheel" viewBox="0 0 510 210">
    <circle cx="255" cy="3" r="166" fill="none" stroke="#c7cdd3" stroke-width="3"/>
    <path d="M135 8A120 120 0 0 0 375 8" fill="none" stroke="var(--ring)" stroke-width="9"/>
    <path d="M144 8A111 111 0 0 0 366 8Z" fill="url(#disc)"/>
    <g>
      <g transform="translate(94 44)"><circle r="31" fill="var(--c1)"/><circle r="27" fill="url(#shine)" stroke="#fff" stroke-width="2.4"/><use href="#i-team" x="-16" y="-16" width="32" height="32" color="var(--c1)"/></g>
      <g transform="translate(127 105)"><circle r="31" fill="var(--c2)"/><circle r="27" fill="url(#shine)" stroke="#fff" stroke-width="2.4"/><use href="#i-money" x="-16" y="-16" width="32" height="32"/></g>
      <g transform="translate(185 152)"><circle r="31" fill="var(--c3)"/><circle r="27" fill="url(#shine)" stroke="#fff" stroke-width="2.4"/><use href="#i-idea" x="-16" y="-16" width="32" height="32"/></g>
      <g transform="translate(255 169)"><circle r="31" fill="var(--c4)"/><circle r="27" fill="url(#shine)" stroke="#fff" stroke-width="2.4"/><use href="#i-gear" x="-16" y="-16" width="32" height="32"/></g>
      <g transform="translate(326 152)"><circle r="31" fill="var(--c5)"/><circle r="27" fill="url(#shine)" stroke="#fff" stroke-width="2.4"/><use href="#i-hands" x="-16" y="-16" width="32" height="32"/></g>
      <g transform="translate(383 105)"><circle r="31" fill="var(--c6)"/><circle r="27" fill="url(#shine)" stroke="#fff" stroke-width="2.4"/><use href="#i-shield" x="-16" y="-16" width="32" height="32"/></g>
      <g transform="translate(415 44)"><circle r="31" fill="var(--c7)"/><circle r="27" fill="url(#shine)" stroke="#fff" stroke-width="2.4"/><use href="#i-search" x="-16" y="-16" width="32" height="32"/></g>
    </g>
  </svg>
  <div class="wheel__label"><div class="wheel__we">WE</div><div class="wheel__value">VALUE</div></div>

  <div class="values">
    <div class="values__row">
      <div class="value value--left"><span class="value__num" style="color:var(--n1)">1</span><div class="value__body"><h3 class="value__title" style="color:var(--t1)">Teamwork</h3><p class="value__text">Collaborating with team members, clients and partners to<br>maintain a high level of communication, accountability and<br>engagement to achieve our common goals.</p></div></div>
      <div class="value value--right"><span class="value__num" style="color:var(--n4)">4</span><div class="value__body"><h3 class="value__title" style="color:var(--t4)">Proactivity</h3><p class="value__text">We hold ourselves accountable in anticipating<br>regulatory changes and keeping you and your<br>plan in compliance.</p></div></div>
    </div>
    <div class="values__row values__row--shaded">
      <div class="value value--left" style="top:2px"><span class="value__num" style="color:var(--n2)">2</span><div class="value__body"><h3 class="value__title" style="color:var(--t2)">Financial Empowerment</h3><p class="value__text">We commit ourselves to providing the best retirement<br>solutions to guide our clients toward financial freedom.</p></div></div>
      <div class="value value--right" style="top:2px"><span class="value__num" style="color:var(--n5)">5</span><div class="value__body"><h3 class="value__title" style="color:var(--t5)">Dedication</h3><p class="value__text">We provide exceptional customer service and ensure<br>that we are friendly, timely and responsive whenever<br>corresponding with our clients.</p></div></div>
      <div class="value value--left" style="top:54px"><span class="value__num" style="color:var(--n3)">3</span><div class="value__body"><h3 class="value__title" style="color:var(--t3)">Knowledge</h3><p class="value__text">Our team of highly trained and credentialed experts work<br>to educate and lead our clients toward success.</p></div></div>
      <div class="value value--right" style="top:54px"><span class="value__num" style="color:var(--n6)">6</span><div class="value__body"><h3 class="value__title" style="color:var(--t6)">Security</h3><p class="value__text">With an emphasis on high technological standards, we<br>lead you toward peace of mind that your savings and<br>investments are protected.</p></div></div>
    </div>
  </div>

  <div class="closing">
    <h3 class="closing__title">Transparency</h3>
    <p class="closing__text">We take pride in representing the retirement plan industry as an open, honest, and socially responsible firm with our clients.</p>
  </div>
  <div class="footer-bar"></div>
</section>

</body>
</html>
```